BRIMCOVE is a New Zealand based aerial imaging company performing mapping, surveying and videography

I would like a business card that is contemporary and clean. The font for the business name is called Gtec Technology and I would like to have the text "AERIAL IMAGING" under the "BRIMCOVE" name in a font similar to URW Gothic or another light modern font. Brimcove performs aerial imaging projects using a hexacopter UAV. Surveying and mapping with 3D Digital Elevation Models are a focus, I also produce aerial photographs and video's including post editing.

Target Market(s)

Industrial plant managers, Property owners, Event organisers.

Industry/Entity Type

Videography

Contact Information for Business Card

BRIMCOVE AERIAL IMAGING. Owner Reid Malloway. Cell: 021 7304169. P.O. Box 8316 Dunedin, New Zealand.

Font styles to use
Other font styles liked:
• Gtec Technology

Colors
9bcb3b
33a6d7
ec1f27

Requirements
Must have
• Modern professional look.
Nice to have
• Perhaps an aerial image of a landscape who's location is not identifiable. Maybe use included image of my hexacopter on the back of the card? Not compulsory though.
Should not have
• Clip Art style images.

```html
<!DOCTYPE html>
<html lang="en">
<head>
<meta charset="utf-8">
<title>Brimcove Aerial Imaging – Business Card</title>
<link href="https://fonts.googleapis.com/css2?family=Orbitron:wght@500;700&family=Questrial&display=swap" rel="stylesheet">
<style>
  :root {
    --bg: #e9e6e1;
    --card: #ffffff;
    --ink: #1f1f1f;
    --charcoal: #2c2c2c;
    --blue: #2e9bcf;
    --blue-deep: #0b7fb6;
    --green: #5cb83a;
    --rule: rgba(255,255,255,.15);
  }
  * { box-sizing: border-box; margin: 0; padding: 0; }
  html, body { width: 1200px; height: 800px; overflow: hidden; }
  body {
    background: var(--bg);
    font-family: "Questrial", sans-serif;
    position: relative;
  }
  .card {
    position: absolute;
    left: 290px;
    width: 620px;
    height: 355px;
    background: var(--card);
    border-radius: 16px;
    overflow: hidden;
    box-shadow: 0 6px 18px rgba(0,0,0,.18);
  }
  .card--front { top: 25px; }
  .card--back { top: 415px; }
  .card svg.shapes { position: absolute; inset: 0; }

  .brand { position: absolute; white-space: nowrap; }
  .brand__name {
    font-family: "Orbitron", sans-serif;
    font-weight: 700;
    color: var(--green);
    letter-spacing: 2px;
    line-height: 1;
  }
  .brand__tag {
    font-family: "Questrial", sans-serif;
    color: var(--ink);
    margin-top: 4px;
    letter-spacing: 1px;
  }
  .card--front .brand { left: 300px; top: 135px; }
  .card--front .brand__name { font-size: 44px; }
  .card--front .brand__tag { font-size: 25px; padding-left: 40px; }

  .card--back .brand { left: 335px; top: 92px; }
  .card--back .brand__name { font-size: 36px; }
  .card--back .brand__tag { font-size: 21px; padding-left: 32px; }

  .person { position: absolute; left: 30px; top: 112px; white-space: nowrap; }
  .person__name {
    font-family: "Orbitron", sans-serif;
    font-weight: 500;
    font-size: 25px;
    color: var(--blue);
    letter-spacing: 1px;
  }
  .person__role {
    font-family: "Orbitron", sans-serif;
    font-weight: 700;
    font-size: 15px;
    color: var(--ink);
    letter-spacing: 1px;
    margin-top: 2px;
  }

  .contact {
    position: absolute;
    display: flex;
    align-items: center;
    gap: 10px;
    color: #fff;
    font-size: 16px;
    white-space: nowrap;
    padding-bottom: 4px;
    border-bottom: 1px solid var(--rule);
  }
  .contact svg { width: 18px; height: 18px; flex: none; }
  .contact--phone { left: 24px; top: 196px; }
  .contact--mobile { left: 24px; top: 224px; }
  .contact--web { left: 200px; top: 196px; }
  .contact--mail { left: 200px; top: 224px; }
  .contact--company { left: 24px; top: 252px; color: var(--blue); }
  .address {
    position: absolute;
    left: 24px;
    top: 284px;
    color: #fff;
    font-size: 16px;
    white-space: nowrap;
  }
</style>
</head>
<body>

  <section class="card card--front" aria-label="Card front">
    <svg class="shapes" viewBox="0 0 620 355" preserveAspectRatio="none" aria-hidden="true">
      <defs>
        <linearGradient id="frontBlue" x1="0" y1="0" x2="0" y2="1">
          <stop offset="0" stop-color="#1aa7d6"/>
          <stop offset="1" stop-color="#0a78ad"/>
        </linearGradient>
      </defs>
      <path d="M0,0 L285,0 C230,90 265,240 455,355 L0,355 Z" fill="url(#frontBlue)"/>
      <path d="M0,168 C60,210 150,300 230,355 L0,355 Z" fill="#ffffff"/>
      <path d="M0,182 C55,220 135,300 205,355 L0,355 Z" fill="var(--charcoal)"/>
    </svg>
    <div class="brand">
      <div class="brand__name">BRIMCOVE</div>
      <div class="brand__tag">Aerial Imaging</div>
    </div>
  </section>

  <section class="card card--back" aria-label="Card back">
    <svg class="shapes" viewBox="0 0 620 355" preserveAspectRatio="none" aria-hidden="true">
      <path d="M0,165 L620,228 L620,355 L0,355 Z" fill="var(--charcoal)"/>
      <path d="M620,40 C600,210 470,325 250,355 L620,355 Z" fill="var(--blue)"/>
      <path d="M620,278 C560,305 480,330 400,355 L620,355 Z" fill="#ffffff"/>
      <path d="M620,290 C565,315 490,338 425,355 L620,355 Z" fill="var(--charcoal)"/>
    </svg>

    <div class="person">
      <div class="person__name">REID MALLOWAY</div>
      <div class="person__role">OWNER</div>
    </div>

    <div class="contact contact--phone">
      <svg viewBox="0 0 20 20"><circle cx="10" cy="10" r="9" fill="none" stroke="#2e9bcf" stroke-width="1.4"/><path d="M7 5.5l2 2-1 1.2c.6 1.3 1.6 2.3 2.9 2.9l1.2-1 2 2-1.2 1.4c-3.4-.3-6.4-3.3-6.7-6.7z" fill="#2e9bcf"/></svg>
      <span>021 7304169</span>
    </div>
    <div class="contact contact--mobile">
      <svg viewBox="0 0 20 20"><rect x="6" y="3" width="8" height="14" rx="1.5" fill="none" stroke="#2e9bcf" stroke-width="1.4"/><circle cx="10" cy="14.5" r=".9" fill="#2e9bcf"/></svg>
      <span>748 52 19 03</span>
    </div>

    <div class="contact contact--web">
      <svg viewBox="0 0 20 20"><circle cx="10" cy="10" r="8" fill="none" stroke="#2e9bcf" stroke-width="1.4"/><ellipse cx="10" cy="10" rx="3.5" ry="8" fill="none" stroke="#2e9bcf" stroke-width="1.2"/><path d="M2 10h16" stroke="#2e9bcf" stroke-width="1.2"/></svg>
      <span>www.harlowmere.com</span>
    </div>
    <div class="contact contact--mail">
      <svg viewBox="0 0 20 20"><rect x="3" y="5" width="14" height="10" rx="1" fill="none" stroke="#2e9bcf" stroke-width="1.4"/><path d="M3 5.5l7 5 7-5" fill="none" stroke="#2e9bcf" stroke-width="1.4"/></svg>
      <span>info@harlowmere.com</span>
    </div>

    <div class="contact contact--company">
      <svg viewBox="0 0 20 20"><path d="M10 2.5a5 5 0 0 1 5 5c0 3.8-5 10-5 10s-5-6.2-5-10a5 5 0 0 1 5-5z" fill="none" stroke="#2e9bcf" stroke-width="1.4"/><circle cx="10" cy="7.5" r="1.7" fill="#2e9bcf"/></svg>
      <span>Harlowmere Consulting Incorporated</span>
    </div>
    <div class="address">P.O. Box 8316 Dunedin, New Zealand</div>

    <div class="brand">
      <div class="brand__name">BRIMCOVE</div>
      <div class="brand__tag">Aerial Imaging</div>
    </div>
  </section>

</body>
</html>
```